Powerpoint Sales and Pre-Sales Decks

We need a GD to support us as we start buillidng many PPT decks - we are a start-up based in London in the Telecomms space

```html
<!DOCTYPE html>
<html lang="en">
<head>
<meta charset="utf-8">
<title>Sales and Pre-Sales Deck Templates</title>
<link href="https://fonts.googleapis.com/css2?family=Lato:wght@300;400;700;900&display=swap" rel="stylesheet">
<style>
:root{
  --page:#eceef1;
  --ink:#2f3642;
  --muted:#8a919c;
  --line:#dfe3e8;
  --dark:#2e3542;
  --darker:#262c37;
  --tile:#3b4556;
  --blue:#3d8fcc;
  --teal:#35a99a;
  --green:#9bbf4a;
  --orange:#ef8b3a;
  --red:#e0523f;
  --navy:#34495e;
  --white:#ffffff;
}
*{box-sizing:border-box;margin:0;padding:0}
html,body{width:1200px;height:3052px;overflow:hidden;background:var(--page);font-family:"Lato",Arial,sans-serif;color:var(--ink)}
.deck{display:grid;grid-template-columns:580px 580px;grid-auto-rows:326px;column-gap:20px;row-gap:14px;padding:3px 10px 0}
.slide{position:relative;width:580px;height:326px;background:var(--white);overflow:hidden;box-shadow:0 1px 3px rgba(0,0,0,.12)}
.slide.dark{background:var(--dark)}
.badge{position:absolute;top:10px;right:12px;width:14px;height:10px;border-radius:2px;background:var(--dark)}
.dark .badge{background:#4a5466}
.title{position:absolute;top:12px;left:0;right:0;text-align:center;font-weight:700;font-size:15px;color:var(--ink)}
.dark .title,.title.light{color:var(--white)}
.sub{position:absolute;left:0;right:0;text-align:center;font-size:6.5px;color:var(--muted)}
.abs{position:absolute}
.txt{font-size:6px;line-height:1.45;color:var(--muted)}
.dark .txt,.txt.light{color:#c3c9d3}
.head{font-size:7px;font-weight:700;margin-bottom:2px}
.c-blue{color:var(--blue)}.c-teal{color:var(--teal)}.c-green{color:var(--green)}.c-orange{color:var(--orange)}.c-red{color:var(--red)}
.center{text-align:center}
.right{text-align:right}
svg{position:absolute;left:0;top:0;overflow:visible}
.price{position:absolute;left:40px;top:48px;width:500px;border-collapse:collapse;font-size:7px;text-align:center}
.price th{color:var(--white);font-weight:700;height:22px}
.price td{height:20px;color:var(--muted);border-bottom:1px solid var(--white)}
.price tr:nth-child(odd) td{background:#f3f5f7}
.price tr:nth-child(even) td{background:#e8ebef}
.price td:first-child{color:var(--ink);font-weight:700;text-align:left;padding-left:8px}
.quote-line{position:absolute;left:70px;height:32px;display:flex;align-items:center}
.quote-word{width:150px;height:32px;border:1px solid #5aa0d6;color:#7fb6e2;font-size:18px;font-weight:300;letter-spacing:2px;display:flex;align-items:center;padding-left:8px;white-space:nowrap}
.quote-bar{height:32px}
</style>
</head>
<body>
<main class="deck">

<section class="slide">
  <div class="badge"></div>
  <h2 class="title">Square Smartart</h2>
  <svg width="580" height="326">
    <rect x="140" y="50" width="300" height="26" fill="var(--navy)"/>
    <rect x="140" y="76" width="75" height="100" fill="var(--blue)"/>
    <rect x="215" y="76" width="75" height="100" fill="var(--teal)"/>
    <rect x="290" y="76" width="75" height="100" fill="var(--green)"/>
    <rect x="365" y="76" width="75" height="100" fill="var(--orange)"/>
  </svg>
  <div class="abs txt light center" style="left:140px;top:58px;width:300px;font-size:7px;font-weight:700">Our core offer</div>
  <div class="abs txt light center" style="left:145px;top:115px;width:65px">Voice</div>
  <div class="abs txt light center" style="left:220px;top:115px;width:65px">Data</div>
  <div class="abs txt light center" style="left:295px;top:115px;width:65px">Cloud</div>
  <div class="abs txt light center" style="left:370px;top:115px;width:65px">Support</div>
  <div class="abs txt right" style="left:30px;top:80px;width:98px"><div class="head c-blue">Title here</div>Short text to describe this point clearly for the client.</div>
  <div class="abs txt" style="left:452px;top:80px;width:98px"><div class="head c-orange">Title here</div>Short text to describe this point clearly for the client.</div>
  <div class="abs txt center" style="left:70px;top:206px;width:440px">Use this slide to show how the four parts of the service fit together. Keep each column short and let the colour guide the eye from left to right across the offer.</div>
</section>

<section class="slide">
  <div class="badge"></div>
  <h2 class="title">Pie chart slide</h2>
  <p class="sub" style="top:32px">Add a short subtitle here</p>
  <svg width="580" height="326">
    <g fill="none" stroke-width="13">
      <circle cx="110" cy="100" r="34" stroke="var(--line)"/>
      <circle cx="110" cy="100" r="34" stroke="var(--blue)" stroke-dasharray="117 214" transform="rotate(-90 110 100)"/>
      <circle cx="230" cy="100" r="34" stroke="var(--line)"/>
      <circle cx="230" cy="100" r="34" stroke="var(--teal)" stroke-dasharray="132 214" transform="rotate(-90 230 100)"/>
      <circle cx="350" cy="100" r="34" stroke="var(--line)"/>
      <circle cx="350" cy="100" r="34" stroke="var(--green)" stroke-dasharray="81 214" transform="rotate(-90 350 100)"/>
      <circle cx="470" cy="100" r="34" stroke="var(--line)"/>
      <circle cx="470" cy="100" r="34" stroke="var(--orange)" stroke-dasharray="158 214" transform="rotate(-90 470 100)"/>
    </g>
    <g font-size="14" font-weight="700" text-anchor="middle" fill="var(--ink)">
      <text x="110" y="105">55%</text><text x="230" y="105">62%</text><text x="350" y="105">38%</text><text x="470" y="105">74%</text>
    </g>
  </svg>
  <div class="abs txt center" style="left:60px;top:150px;width:100px"><div class="head c-blue">Plan</div>Short text to describe this point clearly.</div>
  <div class="abs txt center" style="left:180px;top:150px;width:100px"><div class="head c-teal">Build</div>Short text to describe this point clearly.</div>
  <div class="abs txt center" style="left:300px;top:150px;width:100px"><div class="head c-green">Launch</div>Short text to describe this point clearly.</div>
  <div class="abs txt center" style="left:420px;top:150px;width:100px"><div class="head c-orange">Grow</div>Short text to describe this point clearly.</div>
  <div class="abs txt center" style="left:70px;top:236px;width:440px">Each ring shows one share of the whole. Change the numbers to match your data and keep the labels short so the chart stays easy to read.</div>
</section>

<section class="slide">
  <div class="badge"></div>
  <h2 class="title">Bars slide example</h2>
  <svg width="580" height="326">
    <g stroke="var(--line)" stroke-width="1">
      <line x1="50" y1="60" x2="540" y2="60"/><line x1="50" y1="95" x2="540" y2="95"/><line x1="50" y1="130" x2="540" y2="130"/><line x1="50" y1="165" x2="540" y2="165"/><line x1="50" y1="200" x2="540" y2="200"/>
    </g>
    <g>
      <rect x="70" y="120" width="12" height="80" fill="var(--navy)"/><rect x="84" y="100" width="12" height="100" fill="var(--blue)"/><rect x="98" y="140" width="12" height="60" fill="var(--green)"/>
      <rect x="138" y="90" width="12" height="110" fill="var(--navy)"/><rect x="152" y="130" width="12" height="70" fill="var(--blue)"/><rect x="166" y="110" width="12" height="90" fill="var(--green)"/>
      <rect x="206" y="140" width="12" height="60" fill="var(--navy)"/><rect x="220" y="80" width="12" height="120" fill="var(--blue)"/><rect x="234" y="120" width="12" height="80" fill="var(--green)"/>
      <rect x="274" y="105" width="12" height="95" fill="var(--navy)"/><rect x="288" y="125" width="12" height="75" fill="var(--blue)"/><rect x="302" y="70" width="12" height="130" fill="var(--green)"/>
      <rect x="342" y="130" width="12" height="70" fill="var(--navy)"/><rect x="356" y="95" width="12" height="105" fill="var(--blue)"/><rect x="370" y="115" width="12" height="85" fill="var(--green)"/>
      <rect x="410" y="85" width="12" height="115" fill="var(--navy)"/><rect x="424" y="110" width="12" height="90" fill="var(--blue)"/><rect x="438" y="135" width="12" height="65" fill="var(--green)"/>
      <rect x="478" y="115" width="12" height="85" fill="var(--navy)"/><rect x="492" y="75" width="12" height="125" fill="var(--blue)"/><rect x="506" y="100" width="12" height="100" fill="var(--green)"/>
    </g>
  </svg>
  <div class="abs center" style="left:0;right:0;top:222px;font-size:13px;font-weight:700">Conclusion</div>
  <p class="sub" style="top:240px">Add a short subtitle here</p>
  <div class="abs txt center" style="left:60px;top:258px;width:460px">Sum up what the chart shows in one or two lines. Point to the group that matters most and say what it means for the client and for the next step.</div>
</section>

<section class="slide">
  <div class="badge"></div>
  <h2 class="title">Team slide example</h2>
  <div class="abs" role="img" aria-label="Silhouette of a team member" style="left:232px;top:60px;width:52px;height:210px;background:var(--blue);border-radius:26px 26px 4px 4px"></div>
  <div class="abs" role="img" aria-label="Silhouette of a team member" style="left:296px;top:60px;width:52px;height:210px;background:var(--teal);border-radius:26px 26px 4px 4px"></div>
  <svg width="580" height="326">
    <circle cx="208" cy="80" r="6" fill="var(--blue)"/><circle cx="208" cy="150" r="6" fill="var(--blue)"/><circle cx="208" cy="220" r="6" fill="var(--blue)"/>
    <circle cx="372" cy="80" r="6" fill="var(--teal)"/><circle cx="372" cy="150" r="6" fill="var(--teal)"/><circle cx="372" cy="220" r="6" fill="var(--teal)"/>
  </svg>
  <div class="abs txt right" style="left:60px;top:72px;width:135px"><div class="head c-blue">Sales lead</div>Short text to describe this role clearly.</div>
  <div class="abs txt right" style="left:60px;top:142px;width:135px"><div class="head c-blue">Pre-sales</div>Short text to describe this role clearly.</div>
  <div class="abs txt right" style="left:60px;top:212px;width:135px"><div class="head c-blue">Account team</div>Short text to describe this role clearly.</div>
  <div class="abs txt" style="left:385px;top:72px;width:135px"><div class="head c-teal">Engineering</div>Short text to describe this role clearly.</div>
  <div class="abs txt" style="left:385px;top:142px;width:135px"><div class="head c-teal">Network</div>Short text to describe this role clearly.</div>
  <div class="abs txt" style="left:385px;top:212px;width:135px"><div class="head c-teal">Service desk</div>Short text to describe this role clearly.</div>
  <div class="abs txt center" style="left:90px;top:285px;width:400px">Introduce the people behind the offer and what each one brings.</div>
</section>

<section class="slide">
  <div class="badge"></div>
  <h2 class="title">Bars slide example</h2>
  <svg width="580" height="326">
    <g opacity=".95">
      <path d="M25 230 C55 230 60 120 85 120 C110 120 115 230 145 230Z" fill="var(--navy)"/>
      <path d="M90 230 C120 230 125 95 150 95 C175 95 180 230 210 230Z" fill="var(--blue)"/>
      <path d="M155 230 C185 230 190 135 215 135 C240 135 245 230 275 230Z" fill="var(--teal)"/>
      <path d="M220 230 C250 230 255 80 280 80 C305 80 310 230 340 230Z" fill="var(--green)"/>
      <path d="M285 230 C315 230 320 115 345 115 C370 115 375 230 405 230Z" fill="var(--blue)"/>
      <path d="M350 230 C380 230 385 100 410 100 C435 100 440 230 470 230Z" fill="var(--teal)"/>
      <path d="M415 230 C445 230 450 125 475 125 C500 125 505 230 535 230Z" fill="var(--green)"/>
    </g>
    <line x1="20" y1="230" x2="560" y2="230" stroke="var(--navy)" stroke-width="2"/>
    <g fill="var(--navy)">
      <circle cx="85" cy="98" r="9"/><circle cx="150" cy="73" r="9" fill="var(--blue)"/><circle cx="215" cy="113" r="9" fill="var(--teal)"/><circle cx="280" cy="58" r="9" fill="var(--green)"/><circle cx="345" cy="93" r="9" fill="var(--blue)"/><circle cx="410" cy="78" r="9" fill="var(--teal)"/><circle cx="475" cy="103" r="9" fill="var(--green)"/>
    </g>
    <g font-size="6.5" fill="var(--muted)" text-anchor="middle">
      <text x="85" y="244">Jan</text><text x="150" y="244">Feb</text><text x="215" y="244">Mar</text><text x="280" y="244">Apr</text><text x="345" y="244">May</text><text x="410" y="244">Jun</text><text x="475" y="244">Jul</text>
    </g>
  </svg>
  <div class="abs txt center" style="left:70px;top:268px;width:440px">Each peak marks one month of growth. Swap in your own values and keep the markers above each curve.</div>
</section>

<section class="slide">
  <div class="badge"></div>
  <h2 class="title">Basic pie Smartart</h2>
  <svg width="580" height="326">
    <line x1="210" y1="120" x2="290" y2="175" stroke="var(--line)" stroke-width="2"/>
    <line x1="370" y1="120" x2="290" y2="175" stroke="var(--line)" stroke-width="2"/>
    <circle cx="290" cy="180" r="52" fill="var(--teal)"/>
    <circle cx="205" cy="118" r="34" fill="var(--blue)"/>
    <circle cx="375" cy="118" r="34" fill="var(--green)"/>
    <g fill="var(--blue)"><path d="M150 72 l6 -10 l6 10z"/></g>
    <g fill="var(--green)"><path d="M424 62 l10 5 l-10 5z"/></g>
    <path d="M284 174 l5 5 l9 -10" fill="none" stroke="#fff" stroke-width="3"/>
  </svg>
  <div class="abs txt light center" style="left:175px;top:112px;width:60px">Step one</div>
  <div class="abs txt light center" style="left:345px;top:112px;width:60px">Step two</div>
  <div class="abs txt light center" style="left:250px;top:192px;width:80px">Result</div>
  <div class="abs txt" style="left:40px;top:160px;width:130px"><div class="head c-blue">First idea</div>Short text to describe this point clearly.</div>
  <div class="abs txt right" style="left:410px;top:160px;width:130px"><div class="head c-green">Second idea</div>Short text to describe this point clearly.</div>
  <div class="abs txt center" style="left:90px;top:270px;width:400px">Two inputs join to form one outcome. Keep each label to a few words.</div>
</section>

<section class="slide">
  <div class="badge"></div>
  <h2 class="title">Pie chart slide</h2>
  <svg width="580" height="326">
    <polygon points="59,50 145,50 145,150 102,172 59,150" fill="var(--blue)"/>
    <polygon points="153,50 239,50 239,150 196,172 153,150" fill="var(--teal)"/>
    <polygon points="247,50 333,50 333,150 290,172 247,150" fill="var(--green)"/>
    <polygon points="341,50 427,50 427,150 384,172 341,150" fill="var(--orange)"/>
    <polygon points="435,50 521,50 521,150 478,172 435,150" fill="var(--red)"/>
    <g font-size="18" font-weight="300" fill="#fff" text-anchor="middle">
      <text x="102" y="86">25%</text><text x="196" y="86">40%</text><text x="290" y="86">15%</text><text x="384" y="86">30%</text><text x="478" y="86">25%</text>
    </g>
  </svg>
  <div class="abs txt light center" style="left:64px;top:100px;width:76px">Short text for this value.</div>
  <div class="abs txt light center" style="left:158px;top:100px;width:76px">Short text for this value.</div>
  <div class="abs txt light center" style="left:252px;top:100px;width:76px">Short text for this value.</div>
  <div class="abs txt light center" style="left:346px;top:100px;width:76px">Short text for this value.</div>
  <div class="abs txt light center" style="left:440px;top:100px;width:76px">Short text for this value.</div>
  <div class="abs txt center" style="left:60px;top:200px;width:460px">Five shares side by side make a quick comparison. Change the figures to match your own results and keep the colour for each share the same across the whole deck.</div>
</section>

<section class="slide">
  <div class="badge"></div>
  <div class="abs" style="left:0;top:0;width:580px;height:120px;background:var(--dark)"></div>
  <h2 class="title light" style="top:16px">Keys for success</h2>
  <p class="sub" style="top:36px;color:#aeb6c2">Add a short subtitle here</p>
  <svg width="580" height="326">
    <circle cx="178" cy="120" r="46" fill="var(--blue)"/>
    <circle cx="252" cy="120" r="46" fill="var(--teal)" opacity=".95"/>
    <circle cx="326" cy="120" r="46" fill="var(--green)" opacity=".95"/>
    <circle cx="400" cy="120" r="46" fill="var(--orange)" opacity=".95"/>
  </svg>
  <div class="abs txt light center" style="left:148px;top:105px;width:60px"><div class="head" style="color:#fff">Focus</div>Short note here.</div>
  <div class="abs txt light center" style="left:222px;top:105px;width:60px"><div class="head" style="color:#fff">Speed</div>Short note here.</div>
  <div class="abs txt light center" style="left:296px;top:105px;width:60px"><div class="head" style="color:#fff">Trust</div>Short note here.</div>
  <div class="abs txt light center" style="left:370px;top:105px;width:60px"><div class="head" style="color:#fff">Value</div>Short note here.</div>
  <div class="abs center" style="left:0;right:0;top:196px;font-size:9px;font-weight:700;color:var(--blue)">What drives our results</div>
  <div class="abs txt center" style="left:70px;top:212px;width:440px">Four simple ideas shape every deal we run. Use this slide to open a pitch and set the tone before the detail.</div>
</section>

<section class="slide">
  <div class="badge"></div>
  <div class="abs" style="left:0;top:0;width:580px;height:100px;background:var(--dark)"></div>
  <h2 class="title light" style="top:16px">Keys for success</h2>
  <svg width="580" height="326">
    <rect x="55" y="55" width="110" height="110" fill="var(--blue)"/><polygon points="102,165 118,165 110,174" fill="var(--blue)"/>
    <rect x="175" y="55" width="110" height="110" fill="var(--teal)"/><polygon points="222,165 238,165 230,174" fill="var(--teal)"/>
    <rect x="295" y="55" width="110" height="110" fill="var(--green)"/><polygon points="342,165 358,165 350,174" fill="var(--green)"/>
    <rect x="415" y="55" width="110" height="110" fill="var(--orange)"/><polygon points="462,165 478,165 470,174" fill="var(--orange)"/>
    <g fill="none" stroke="#fff" stroke-width="2">
      <circle cx="110" cy="75" r="7"/><path d="M224 70 h12 v10 h-12z"/><path d="M344 80 l6 -10 l6 10z"/><path d="M464 75 l4 4 l8 -8"/>
    </g>
  </svg>
  <div class="abs txt light center" style="left:62px;top:92px;width:96px"><div class="head" style="color:#fff">Clear goals</div>Short text to describe this point clearly.</div>
  <div class="abs txt light center" style="left:182px;top:92px;width:96px"><div class="head" style="color:#fff">Good tools</div>Short text to describe this point clearly.</div>
  <div class="abs txt light center" style="left:302px;top:92px;width:96px"><div class="head" style="color:#fff">Strong team</div>Short text to describe this point clearly.</div>
  <div class="abs txt light center" style="left:422px;top:92px;width:96px"><div class="head" style="color:#fff">Happy clients</div>Short text to describe this point clearly.</div>
  <div class="abs txt center" style="left:70px;top:200px;width:440px">Walk the client through each key in turn. A short line under each box is enough; keep the detail for the talk track.</div>
</section>

<section class="slide">
  <div class="badge"></div>
  <div class="abs" style="left:0;top:0;width:580px;height:95px;background:var(--dark)"></div>
  <h2 class="title light" style="top:16px">Five goals to 2016</h2>
  <svg width="580" height="326">
    <rect x="60" y="52" width="84" height="56" fill="var(--tile)"/>
    <rect x="154" y="52" width="84" height="56" fill="var(--tile)"/>
    <rect x="248" y="52" width="84" height="56" fill="var(--tile)"/>
    <rect x="342" y="52" width="84" height="56" fill="var(--tile)"/>
    <rect x="436" y="52" width="84" height="56" fill="var(--tile)"/>
    <g fill="#f6f7f9"><rect x="60" y="108" width="84" height="90"/><rect x="154" y="108" width="84" height="90"/><rect x="248" y="108" width="84" height="90"/><rect x="342" y="108" width="84" height="90"/><rect x="436" y="108" width="84" height="90"/></g>
    <rect x="60" y="198" width="84" height="4" fill="var(--blue)"/><rect x="154" y="198" width="84" height="4" fill="var(--teal)"/><rect x="248" y="198" width="84" height="4" fill="var(--green)"/><rect x="342" y="198" width="84" height="4" fill="var(--orange)"/><rect x="436" y="198" width="84" height="4" fill="var(--red)"/>
    <g fill="none" stroke="#fff" stroke-width="2">
      <rect x="94" y="72" width="16" height="16" rx="3"/><path d="M196 70 v20 M188 80 h16"/><circle cx="290" cy="80" r="8"/><path d="M376 88 l8 -16 l8 16z"/><path d="M470 80 l5 5 l10 -10"/>
    </g>
  </svg>
  <div class="abs txt center" style="left:64px;top:118px;width:76px"><div class="head c-blue">Goal one</div>Short text to describe this goal.</div>
  <div class="abs txt center" style="left:158px;top:118px;width:76px"><div class="head c-teal">Goal two</div>Short text to describe this goal.</div>
  <div class="abs txt center" style="left:252px;top:118px;width:76px"><div class="head c-green">Goal three</div>Short text to describe this goal.</div>
  <div class="abs txt center" style="left:346px;top:118px;width:76px"><div class="head c-orange">Goal four</div>Short text to describe this goal.</div>
  <div class="abs txt center" style="left:440px;top:118px;width:76px"><div class="head c-red">Goal five</div>Short text to describe this goal.</div>
  <div class="abs txt center" style="left:70px;top:230px;width:440px">Set out the targets for the year ahead in five short steps.</div>
</section>

<section class="slide">
  <div class="badge"></div>
  <h2 class="title">Price Table</h2>
  <table class="price">
    <tr><th style="background:var(--navy)">Plan</th><th style="background:var(--blue)">Starter</th><th style="background:var(--teal)">Standard</th><th style="background:var(--green)">Business</th><th style="background:var(--orange)">Premium</th><th style="background:var(--red)">Enterprise</th></tr>
    <tr><td>Lines</td><td>5</td><td>20</td><td>50</td><td>100</td><td>Custom</td></tr>
    <tr><td>Data</td><td>10 GB</td><td>50 GB</td><td>200 GB</td><td>500 GB</td><td>Unlimited</td></tr>
    <tr><td>Calls</td><td>UK</td><td>UK</td><td>UK + EU</td><td>Global</td><td>Global</td></tr>
    <tr><td>Support</td><td>Email</td><td>Email</td><td>Phone</td><td>24/7</td><td>Dedicated</td></tr>
    <tr><td>Setup</td><td>Free</td><td>Free</td><td>Free</td><td>Free</td><td>Free</td></tr>
    <tr><td>Monthly</td><td>£29</td><td>£79</td><td>£149</td><td>£299</td><td>Quote</td></tr>
  </table>
  <div class="abs txt center" style="left:70px;top:262px;width:440px">Prices shown are examples only. Edit the rows to match the plans you offer to each client.</div>
</section>

<section class="slide">
  <div class="badge"></div>
  <h2 class="title">Arrow Slide Example</h2>
  <svg width="580" height="326">
    <polygon points="0,55 0,85 250,120 300,120 312,109 300,98 250,98" fill="var(--navy)"/>
    <polygon points="0,105 0,135 250,153 300,153 312,142 300,131 250,131" fill="var(--blue)"/>
    <polygon points="0,165 0,195 250,186 300,186 312,175 300,164 250,164" fill="var(--teal)"/>
    <polygon points="0,225 0,255 250,219 300,219 312,208 300,197 250,197" fill="var(--green)"/>
    <polygon points="0,275 0,305 250,252 300,252 312,241 300,230 250,230" fill="var(--orange)"/>
  </svg>
  <div class="abs txt" style="left:330px;top:104px;width:200px"><span class="head" style="color:var(--navy)">Point one</span> short text here.</div>
  <div class="abs txt" style="left:330px;top:137px;width:200px"><span class="head c-blue">Point two</span> short text here.</div>
  <div class="abs txt" style="left:330px;top:170px;width:200px"><span class="head c-teal">Point three</span> short text here.</div>
  <div class="abs txt" style="left:330px;top:203px;width:200px"><span class="head c-green">Point four</span> short text here.</div>
  <div class="abs txt" style="left:330px;top:236px;width:200px"><span class="head c-orange">Point five</span> short text here.</div>
</section>

<section class="slide">
  <div class="badge"></div>
  <h2 class="title">Text Slide</h2>
  <p class="sub" style="top:32px">Add a short subtitle here</p>
  <div class="abs txt" style="left:50px;top:56px;width:480px">
    <p style="margin-bottom:8px">We help growing firms stay connected. Our network gives each team fast, stable lines and clear pricing, with one point of contact for every site. This paragraph sets out the main message of the deck in a few plain sentences.</p>
    <p style="margin-bottom:8px">Start with the problem the client faces today. Explain the cost of slow links, missed calls and split suppliers, then show how a single service removes that pain and frees the team to focus on their own work.</p>
    <p style="margin-bottom:8px">Next, describe how the move works. We plan the switch with the client, test each line before go live and keep the old service running until the new one is ready, so there is no gap in service at any point.</p>
    <p>Close with the next step. Offer a short call to review needs and share a clear quote within a week.</p>
  </div>
</section>

<section class="slide">
  <div class="badge"></div>
  <h2 class="title">Two columns text slide</h2>
  <p class="sub" style="top:32px">Add a short subtitle here</p>
  <div class="abs txt" style="left:50px;top:56px;width:230px">
    <p style="margin-bottom:8px">The first column holds the main story. Say what the client needs and why it matters now, in plain words they will use themselves.</p>
    <p style="margin-bottom:8px">Add proof where you can: a short result, a time saved or a cost cut from a similar project we have run.</p>
    <p>Keep each paragraph to a few lines so the slide still reads well from the back of the room.</p>
  </div>
  <div class="abs txt" style="left:300px;top:56px;width:230px">
    <p style="margin-bottom:8px">The second column holds the detail. List what is included, how long setup takes and who the client will work with day to day.</p>
    <p style="margin-bottom:8px">Note any options or add-ons here, with a short line on when each one makes sense.</p>
    <p>End with one clear next step and a date to meet again.</p>
  </div>
</section>

<section class="slide">
  <div class="badge"></div>
  <h2 class="title">Three columns text slide</h2>
  <p class="sub" style="top:32px">Add a short subtitle here</p>
  <div class="abs txt" style="left:45px;top:56px;width:150px">
    <p style="margin-bottom:8px">Column one sets the scene. Describe where the client is today and what holds them back.</p>
    <p>Keep it short and in their own words.</p>
  </div>
  <div class="abs txt" style="left:215px;top:56px;width:150px">
    <p style="margin-bottom:8px">Column two shows the plan. Set out each step of the move and who owns it.</p>
    <p>Add a rough time for each step.</p>
  </div>
  <div class="abs txt" style="left:385px;top:56px;width:150px">
    <p style="margin-bottom:8px">Column three shows the gain. Name the result the client can expect after launch.</p>
    <p>Close with a clear next step.</p>
  </div>
</section>

<section class="slide dark">
  <div class="badge"></div>
  <div class="quote-line" style="top:100px"><div class="quote-word">ONE SIMPLE</div><div class="quote-bar" style="width:290px;background:var(--teal)"></div></div>
  <div class="quote-line" style="top:142px"><div class="quote-word">IDEA CAN</div><div class="quote-bar" style="width:250px;background:var(--blue)"></div></div>
  <div class="quote-line" style="top:184px"><div class="quote-word">CHANGE ALL</div><div class="quote-bar" style="width:210px;background:var(--green)"></div></div>
</section>

<section class="slide dark">
  <div class="badge"></div>
  <h2 class="title">Glyph Library</h2>
  <svg width="580" height="326">
    <defs>
      <pattern id="icon-grid" width="20" height="18" patternUnits="userSpaceOnUse">
        <rect x="6" y="5" width="7" height="7" rx="1.5" fill="#c9d0da"/>
      </pattern>
      <pattern id="icon-grid-b" width="40" height="36" patternUnits="userSpaceOnUse">
        <circle cx="9.5" cy="8.5" r="3.8" fill="#c9d0da"/>
        <path d="M26 12 l4 -8 l4 8z" fill="#c9d0da"/>
      </pattern>
    </defs>
    <rect x="40" y="44" width="500" height="252" fill="url(#icon-grid)" opacity=".55"/>
    <rect x="40" y="44" width="500" height="252" fill="url(#icon-grid-b)" opacity=".8"/>
  </svg>
</section>

<section class="slide dark">
  <div class="badge"></div>
  <svg width="580" height="326">
    <path d="M278 152 h6 v16 h-6z M286 152 l6 -10 c2 -3 6 -2 5 2 l-2 6 h8 c3 0 4 2 3 5 l-3 10 c-1 2 -2 3 -4 3 h-13z" fill="#fff"/>
  </svg>
  <h2 class="title light" style="top:180px;font-size:16px">Thanks for your time</h2>
  <div class="abs txt center" style="left:150px;top:204px;width:280px">Questions are welcome. We will follow up with a short summary and the next steps for your team.</div>
</section>

</main>
</body>
</html>
```